Criação de Papelaria Profissional para Roupas, Jóias & acessórios
A empresa queria:
" Locamos roupas para madrinhas , formandas e convidados de gala "

```html
<!DOCTYPE html>
<html lang="pt-BR">
<head>
<meta charset="utf-8">
<title>Véu de Gala — Cartão de Visita</title>
<link rel="stylesheet" href="https://fonts.googleapis.com/css2?family=Raleway:wght@300;400;600&display=swap">
<style>
  :root {
    --page-bg: #ececec;
    --card-bg: #ffffff;
    --card-shade: #f3f2f0;
    --gold: #b8913f;
    --gold-light: #e0c581;
    --ink: #8a8a8a;
    --ink-soft: #a6a6a6;
  }
  * { margin: 0; padding: 0; box-sizing: border-box; }
  html, body {
    width: 1200px; height: 1200px; overflow: hidden;
    background: var(--page-bg);
    font-family: "Raleway", sans-serif;
  }
  .stage {
    width: 1200px; height: 1200px;
    display: flex; align-items: center; justify-content: center;
  }
  .business-card {
    position: relative;
    width: 1040px; height: 578px;
    background: linear-gradient(180deg, var(--card-bg) 0%, var(--card-shade) 100%);
    box-shadow: 0 14px 40px rgba(0,0,0,0.12);
    overflow: hidden;
  }
  .card-ornament {
    position: absolute; right: -60px; top: -40px;
    width: 560px; height: 620px;
    background: radial-gradient(ellipse at 60% 45%, rgba(200,200,200,0.28) 0%, rgba(230,230,230,0.12) 45%, rgba(255,255,255,0) 70%);
  }
  .brand {
    position: absolute; left: 0; top: 0;
    width: 520px; height: 560px;
    display: flex; flex-direction: column; align-items: center; justify-content: center;
    gap: 26px;
  }
  .brand-mark {
    width: 70px; height: 70px; border-radius: 50%;
    border: 3px solid var(--gold);
  }
  .brand-name {
    font-weight: 400; font-size: 62px; letter-spacing: 3px;
    color: var(--gold); text-transform: uppercase;
  }
  .contact {
    position: absolute; left: 560px; top: 88px;
    display: flex; flex-direction: column;
  }
  .contact-row {
    display: flex; align-items: flex-start; gap: 26px;
    font-size: 22px; font-weight: 300; color: var(--ink-soft);
    line-height: 1.45; margin-bottom: 12px;
  }
  .contact-row svg { flex: none; width: 26px; height: 26px; margin-top: 3px; fill: var(--gold); }
  .person { margin-bottom: 44px; }
  .person-name { font-size: 24px; font-weight: 600; color: var(--gold); line-height: 1.1; }
  .person-role { font-size: 19px; font-weight: 400; color: var(--ink); }
  .row-gap { margin-top: 10px; }
  .gold-edge {
    position: absolute; left: 0; right: 0; bottom: 0; height: 14px;
    background: linear-gradient(90deg, var(--gold) 0%, var(--gold-light) 50%, var(--gold) 100%);
  }
  .gold-edge::before {
    content: ""; position: absolute; left: 0; right: 0; top: -10px; height: 2px;
    background: var(--gold-light);
  }
</style>
</head>
<body>
<main class="stage">
  <article class="business-card">
    <div class="card-ornament" role="img" aria-label="Ornamento floral suave em cinza claro ao fundo"></div>

    <section class="brand">
      <span class="brand-mark"></span>
      <h1 class="brand-name">Véu de Gala</h1>
    </section>

    <section class="contact">
      <div class="contact-row person">
        <svg viewBox="0 0 24 24"><circle cx="12" cy="7" r="5"/><path d="M2 23c0-6 4.5-9 10-9s10 3 10 9z"/></svg>
        <div>
          <p class="person-name">Marina Soares</p>
          <p class="person-role">Cargo</p>
        </div>
      </div>

      <div class="contact-row">
        <svg viewBox="0 0 24 24"><path d="M3 9c0-3 4-5 9-5s9 2 9 5v2h-5V8.5C14.5 8 9.5 8 8 8.5V11H3z"/><path d="M6 12h12l2 9H4z"/></svg>
        <span>(12) 3400-5500</span>
      </div>
      <div class="contact-row">
        <svg viewBox="0 0 24 24"><circle cx="12" cy="12" r="10"/></svg>
        <span>(12) 98000-4411</span>
      </div>
      <div class="contact-row">
        <svg viewBox="0 0 24 24"><path d="M2 5h20v14H2z" fill="none" stroke="#b8913f" stroke-width="2"/><path d="M2 5l10 8 10-8" fill="none" stroke="#b8913f" stroke-width="2"/></svg>
        <span>email@seuemail.com</span>
      </div>
      <div class="contact-row row-gap">
        <svg viewBox="0 0 24 24"><path d="M12 1a8 8 0 0 0-8 8c0 6 8 14 8 14s8-8 8-14a8 8 0 0 0-8-8zm0 11a3 3 0 1 1 0-6 3 3 0 0 1 0 6z"/></svg>
        <span>R. das Acácias, Nº 48<br>Centro, Vale Azul - SP</span>
      </div>
      <div class="contact-row row-gap">
        <svg viewBox="0 0 24 24"><circle cx="12" cy="12" r="10" fill="none" stroke="#b8913f" stroke-width="2"/><path d="M2 12h20M12 2c4 4 4 16 0 20M12 2c-4 4-4 16 0 20" fill="none" stroke="#b8913f" stroke-width="1.6"/></svg>
        <span>www.seusite.com</span>
      </div>
    </section>

    <div class="gold-edge"></div>
  </article>
</main>
</body>
</html>
```